Car rental website design for a UAE car rental company

This project is about creating a new website design for a car rental company located in Dubai (United Arab Emirates), I opened the same project a few months ago but I didn't receive a lot of appealing entries so I closed it but this time I am marking the project as guaranteed to avoid such situation again, if you have already provided a design before then please re-submit again on this project so that it is considered while reviewing all the designs

A few important things:

1- We need a simple non-complex design
2- The final deliverable would be 2 screens (PSD, JPEG ... etc), the first screen is for the home page and the second screen is for an internal page
3- The home page must have a section that end users can use to rent a car online directly from the home page instead of going into some inner pages
4- The current website is very old and not very appealing so avoid creating a similar design (www.quarvin-drive.example)
5- The name is Quarvin but the company rents normal cars (no Limousin cars will be rented) so avoid adding any fancy cars in the images/graphics used in the design, just normal end users cars
6- The expected pages would be: home, About us, Our team, Strategy, Contact us and links to social media pages
7- The attachments include the company's logo and some screens from other car rental companies that provide online rentals/payments

If you have any questions please feel free to ask and please note that we will need the designs urgently

Thanks

Target Market(s)

Dubai - United Arab Emirates

Industry/Entity Type

It Company

Number of Pages Required

2 page

Font styles to use
Sans Serif

Requirements
Must have
• Check the project details
Nice to have
Should not have

```html
<!DOCTYPE html>
<html lang="en">
<head>
<meta charset="utf-8">
<title>Quarvin – Rent A Car</title>
<link rel="stylesheet" href="https://fonts.googleapis.com/css2?family=Open+Sans:wght@400;600;700&family=Questrial&display=swap">
<style>
  :root {
    --crimson: #a3103c;
    --crimson-dark: #8c0c33;
    --sage: #8d9b91;
    --sage-light: #a9b5ad;
    --ink: #2b2b2b;
    --ink-soft: #555;
    --line: #c9c9c9;
    --paper: #ffffff;
    --field: #fafafa;
    --pill: #7c8a80;
    --dot: #8a8f94;
  }
  * { box-sizing: border-box; margin: 0; padding: 0; }
  html, body { width: 1200px; height: 920px; overflow: hidden; background: var(--paper); }
  body { position: relative; font-family: "Open Sans", Arial, sans-serif; color: var(--ink); }
  .abs { position: absolute; }

  /* header */
  .site-header { position: absolute; left: 0; top: 0; width: 1200px; height: 103px; background: var(--paper); }
  .brand { position: absolute; left: 98px; top: 14px; display: flex; align-items: center; gap: 10px; }
  .brand-mark { width: 30px; height: 30px; background: var(--crimson); }
  .brand-name { font-family: "Questrial", sans-serif; font-size: 27px; color: var(--sage); line-height: 1; }
  .brand-tag { position: absolute; left: 138px; top: 50px; font-size: 12px; font-weight: 600; color: var(--crimson); letter-spacing: 1px; }
  .main-nav { position: absolute; left: 376px; top: 42px; display: flex; gap: 30px; font-family: "Questrial", sans-serif; font-size: 16px; color: var(--ink-soft); }
  .main-nav a { color: inherit; text-decoration: none; position: relative; }
  .main-nav a.is-active { color: var(--crimson); }
  .main-nav a.is-active::after { content: ""; position: absolute; left: 0; right: 0; bottom: -8px; height: 3px; background: var(--crimson); }
  .account-links { position: absolute; right: 75px; top: 10px; font-size: 11px; color: var(--ink-soft); letter-spacing: .3px; }
  .social { position: absolute; display: flex; gap: 5px; }
  .social span { width: 23px; height: 23px; border-radius: 50%; background: var(--dot); display: block; }
  .social-top { right: 75px; top: 40px; }

  /* hero */
  .hero { position: absolute; left: 0; top: 103px; width: 1200px; height: 427px;
    background: linear-gradient(180deg, #9aa6b8 0%, #c9c6cc 30%, #e6ddd6 52%, #b9b2b0 64%, #8f8a92 100%); }
  .hero-title { position: absolute; left: 0; width: 1200px; top: 132px; text-align: center; font-family: "Questrial", sans-serif; font-size: 38px; color: #111; }
  .hero-title b { font-family: "Open Sans", sans-serif; font-weight: 700; }
  .hero-lead { position: absolute; left: 0; width: 1200px; top: 192px; text-align: center; font-family: "Questrial", sans-serif; font-size: 14px; line-height: 22px; color: #111; }
  .hero-phone { position: absolute; left: 426px; top: 254px; width: 348px; height: 56px; border-radius: 28px; background: var(--pill);
    color: #f2f2f2; font-family: "Open Sans", sans-serif; font-weight: 600; font-size: 38px; text-align: center; line-height: 56px; }

  /* booking */
  .booking { position: absolute; left: 66px; top: 528px; width: 1060px; height: 250px; background: var(--paper); }
  .tab { position: absolute; top: 2px; height: 44px; color: #fff; font-size: 15px; line-height: 44px; text-align: center; font-family: "Questrial", sans-serif; }
  .tab-book { left: 11px; width: 147px; background: var(--crimson); }
  .tab-book::after { content: ""; position: absolute; left: 50%; bottom: -8px; margin-left: -8px; border: 8px solid transparent; border-bottom: 0; border-top-color: var(--crimson); }
  .tab-manage { left: 162px; width: 331px; background: var(--sage-light); }
  .step { position: absolute; width: 33px; height: 41px; border: 1px solid var(--crimson); color: var(--crimson); font-family: "Questrial", sans-serif; font-size: 20px; text-align: center; line-height: 39px; box-shadow: inset 0 0 0 3px #fff, inset 0 0 0 4px #e7c4cf; }
  .label { position: absolute; font-size: 14px; font-weight: 600; color: #222; text-transform: uppercase; }
  .label small { font-size: 12px; font-weight: 400; text-transform: none; color: var(--ink-soft); }
  .hint { position: absolute; font-size: 12px; color: var(--crimson); }
  .field { position: absolute; height: 30px; border: 1px solid var(--line); background: var(--paper); font-size: 12px; color: #777; padding-left: 10px; line-height: 28px; border-radius: 2px; }
  .field svg { position: absolute; right: 8px; top: 8px; }
  .check { position: absolute; font-size: 12.5px; color: var(--ink-soft); display: flex; align-items: center; gap: 8px; }
  .check i { width: 12px; height: 12px; border: 1px solid #aaa; background: #eee; display: block; }
  .help { width: 17px; height: 17px; border-radius: 50%; background: #bbb; color: #fff; font-size: 11px; font-weight: 700; text-align: center; line-height: 17px; font-style: normal; display: inline-block; }
  .quote-btn { position: absolute; left: 752px; top: 168px; width: 284px; height: 38px; background: var(--crimson); color: #fff; font-weight: 700; font-size: 14px; text-align: center; line-height: 38px; border-radius: 2px; }

  /* footer */
  .footer-nav { position: absolute; left: 0; top: 778px; width: 1200px; height: 32px; background: var(--sage); display: flex; justify-content: center; gap: 28px; font-family: "Questrial", sans-serif; font-size: 15px; color: #fff; line-height: 32px; }
  .newsletter-icon { position: absolute; left: 74px; top: 840px; }
  .newsletter-title { position: absolute; left: 145px; top: 842px; font-size: 14.5px; font-weight: 700; color: #222; }
  .newsletter-sub { position: absolute; left: 145px; top: 862px; font-size: 12px; color: var(--ink-soft); }
  .newsletter-input { position: absolute; left: 455px; top: 846px; width: 238px; height: 31px; border: 1px solid var(--line); border-right: 0; font-size: 12px; color: #666; padding-left: 12px; line-height: 29px; }
  .newsletter-btn { position: absolute; left: 692px; top: 846px; width: 74px; height: 31px; background: var(--crimson); color: #fff; font-size: 12px; font-weight: 600; text-align: center; line-height: 31px; }
  .social-bottom { right: 75px; top: 840px; }
  .copyright { position: absolute; right: 75px; top: 870px; font-size: 12px; color: var(--ink-soft); }
</style>
</head>
<body>

<header class="site-header">
  <div class="brand"><span class="brand-mark"></span><span class="brand-name">Quarvin</span></div>
  <div class="brand-tag">Rent A Car</div>
  <nav class="main-nav">
    <a class="is-active" href="#">HOME</a><a href="#">ABOUT US</a><a href="#">OUR TEAM</a><a href="#">STRATEGY</a><a href="#">CONTACT US</a>
  </nav>
  <div class="account-links">LOGIN &nbsp;|&nbsp; REGISTER</div>
  <div class="social social-top" aria-label="Social media links"><span></span><span></span><span></span><span></span><span></span></div>
</header>

<section class="hero" role="img" aria-label="Photo of two everyday sedans, one orange and one red, facing each other on a wooden deck under a cloudy sky">
  <h1 class="hero-title"><b>Quarvin -</b> Rent A Car</h1>
  <p class="hero-lead">AS DUBAI IS EXPECTED TO WELCOME MILLIONS OF<br>TOURISTS AND VISITORS, CAR RENTAL INDUSTRY IS BELIEVED TO ESCALATE MORE RAPIDLY IN THE REGION.</p>
  <div class="hero-phone">971 4 555 0192</div>
</section>

<section class="booking">
  <div class="tab tab-book">BOOK A CAR</div>
  <div class="tab tab-manage">VIEW/MODIFY/CANCEL A RESERVATION</div>

  <div class="step" style="left:34px;top:79px">01</div>
  <div class="label" style="left:80px;top:75px">Pick-up location <small>(City,State or Airport Code)</small></div>
  <div class="hint" style="left:80px;top:96px">Previous Searches</div>
  <div class="field" style="left:82px;top:124px;width:282px"></div>
  <div class="hint" style="left:80px;top:158px">Help me find a rental location</div>
  <div class="check" style="left:82px;top:183px"><i></i>Return car to different Quarvin location <em class="help">?</em></div>

  <div class="step" style="left:394px;top:79px">02</div>
  <div class="label" style="left:440px;top:75px">Pick-up date and time:</div>
  <div class="field" style="left:442px;top:101px;width:136px">DD/MM/YY
    <svg width="14" height="13" viewBox="0 0 14 13"><rect x=".5" y="1.5" width="13" height="11" fill="none" stroke="#aaa"/><rect x="0" y="1" width="14" height="3" fill="#bbb"/></svg></div>
  <div class="field" style="left:588px;top:101px;width:138px">HH:MM
    <svg width="8" height="13" viewBox="0 0 8 13"><path d="M1 5l3-4 3 4M1 8l3 4 3-4" fill="none" stroke="#aaa"/></svg></div>
  <div class="label" style="left:440px;top:146px">Return date and time:</div>
  <div class="field" style="left:442px;top:171px;width:136px">DD/MM/YY
    <svg width="14" height="13" viewBox="0 0 14 13"><rect x=".5" y="1.5" width="13" height="11" fill="none" stroke="#aaa"/><rect x="0" y="1" width="14" height="3" fill="#bbb"/></svg></div>
  <div class="field" style="left:588px;top:171px;width:138px">HH:MM
    <svg width="8" height="13" viewBox="0 0 8 13"><path d="M1 5l3-4 3 4M1 8l3 4 3-4" fill="none" stroke="#aaa"/></svg></div>

  <div class="label" style="left:752px;top:75px">Hire car type: <em class="help">?</em></div>
  <div class="field" style="left:752px;top:103px;width:284px">Show Me All
    <svg width="14" height="10" viewBox="0 0 14 10" style="top:10px"><path d="M1 2l6 6 6-6" fill="none" stroke="#555" stroke-width="1.6"/></svg></div>
  <div class="check" style="left:752px;top:141px"><i></i>Apply a discount code <em class="help">?</em></div>
  <div class="quote-btn">GET A QUOTE</div>
</section>

<nav class="footer-nav"><span>HOME</span><span>ABOUT US</span><span>OUR TEAM</span><span>STRATEGY</span><span>CONTACT US</span></nav>

<svg class="newsletter-icon" width="58" height="34" viewBox="0 0 58 34" aria-hidden="true">
  <rect x="20" y="4" width="36" height="26" fill="none" stroke="#8d9b91" stroke-width="2"/>
  <path d="M20 4l18 14 18-14" fill="none" stroke="#8d9b91" stroke-width="2"/>
  <path d="M2 12h14M6 18h10M0 24h16" stroke="#8d9b91" stroke-width="2"/>
</svg>
<div class="newsletter-title">SIGN UP TO QUARVIN EMAIL NEWSLETTER</div>
<div class="newsletter-sub">Enter your email &amp; give me latest news &amp; updates</div>
<div class="newsletter-input">Enter your email</div>
<div class="newsletter-btn">SIGN UP</div>
<div class="social social-bottom" aria-label="Social media links"><span></span><span></span><span></span><span></span><span></span></div>
<div class="copyright">©2015 Quarvin. All Rights Reserved.</div>

</body>
</html>
```